Gladly Call Corwin Consulting needs a new and exciting customer online experience (Webpage)

Gladly Call Corwin is a new and exciting IT and Telecoms business. We aim to help business with all of its technology needs.

The business has only been around less than 12 months and a page was developed to give some online presence, but now its time for a refresh. The page is very bland and boring. It needs some creative zing to give it that pop whilst maintaining a professional appeal.

Our current page can be found at www.gladlycallcorwin.example.au

I have included below some of our current marketing. I've included our business cards and some of messages on hold we are running.

Target Market(s)

Small to medium business, small enterprise

Industry/Entity Type

Business

Number of Pages Required

5+ page

Font styles to use
Sans Serif

Requirements
Must have
• The page must have some colour. IT and Telecoms can be mundane and boring. We want people to be engaged in their IT and Telecoms. We want them to feel as passionate about their IT and Telecoms as we do.
• It must have the following pages: Home, About Us, Services We provide, Contact Us and our Blog Page.
• The contact us should have an option to complete an online form which is delivered to our enquiries email.
• We would also like to have our social media links for Chatterbook, WorkWeave and Quorra plus. The pages must also contain a link to our privacy policy located near the bottom of the page

```html
<!DOCTYPE html>
<html lang="en">
<head>
<meta charset="utf-8">
<title>Gladly Call Corwin Consulting</title>
<link href="https://fonts.googleapis.com/css2?family=Raleway:wght@300;400;500;600&display=swap" rel="stylesheet">
<style>
:root{
  --blue:#29a9e1;
  --ink:#222a30;
  --muted:#9aa3aa;
  --white:#ffffff;
  --band-light:#f2f2f2;
  --band-cool:#f2f5f8;
  --footer:#15232f;
  --footer-base:#101b24;
  --footer-text:#5f7383;
}
*{margin:0;padding:0;box-sizing:border-box}
html,body{width:821px;height:1200px;overflow:hidden}
body{position:relative;font-family:'Raleway',sans-serif;background:var(--white);color:var(--ink)}
.abs{position:absolute}
a{color:inherit;text-decoration:none}

/* header */
.site-header{left:0;top:0;width:821px;height:52px;background:var(--white)}
.brand{left:54px;top:15px;display:flex;align-items:center;gap:6px}
.brand-dot{width:10px;height:10px;border-radius:50%;background:var(--blue)}
.brand-name{font-size:10px;font-weight:500;color:var(--ink);line-height:1.15}
.nav{left:450px;top:0;height:52px;display:flex;font-size:11px}
.nav a{display:block;height:52px;line-height:48px;padding:0 12px;color:var(--ink)}
.nav a.active{background:var(--blue);color:var(--white);position:relative;width:53px;text-align:center;padding:0}
.nav a.active::after{content:"";position:absolute;left:23px;bottom:0;border:4px solid transparent;border-bottom-color:var(--white)}

/* hero */
.hero{left:0;top:52px;width:821px;height:339px;background:linear-gradient(90deg,#1f8fc0 0%,#2aa6d8 45%,#1b7fad 100%)}
.hero-art{left:384px;top:52px;width:437px;height:339px;background:radial-gradient(circle at 55% 55%,#6cc7ea 0%,#2a8fc0 45%,#13283a 100%)}
.hero-title{left:54px;top:126px;font-size:45px;font-weight:300;color:var(--white);line-height:54px;letter-spacing:.3px}
.hero-sub{left:54px;top:246px;font-size:16.5px;font-weight:400;color:var(--white);line-height:18px}
.hero-btn{left:54px;top:308px;width:50px;height:28px;border:1px solid #1b4f6d;color:var(--white);font-size:9px;line-height:26px;text-align:center}
.slider-dots{left:382px;top:371px;display:flex;gap:4px}
.slider-dots span{width:18px;height:2px;background:rgba(255,255,255,.4)}
.slider-dots span.on{background:#111}

/* sections */
.band-intro{left:0;top:391px;width:821px;height:157px;background:var(--band-light)}
.band-features{left:0;top:548px;width:821px;height:444px;background:var(--band-cool)}
.section-title{left:115px;font-size:24px;font-weight:300;color:var(--ink);letter-spacing:.3px}
.section-kicker{left:115px;font-size:13.5px;font-weight:400;color:var(--blue);text-transform:uppercase}
.intro-copy{left:115px;top:474px;width:600px;font-size:9px;line-height:17.4px;color:var(--muted)}

.feature-icon{width:42px;height:42px;border-radius:50%;background:var(--white);border:1px solid #e3e8ec;display:flex;align-items:center;justify-content:center}
.feature-title{left:115px;font-size:11px;font-weight:500;color:var(--ink);text-transform:uppercase}
.feature-copy{left:115px;width:280px;font-size:9px;line-height:17.4px;color:var(--muted)}

.tablet{left:446px;top:654px;width:303px;height:338px;background:#0b0b0b;border-radius:14px 14px 0 0}
.tablet-screen{left:466px;top:696px;width:265px;height:296px;background:radial-gradient(circle at 50% 50%,#e6f5fc 0%,#8ccfee 55%,#3d9fd2 100%)}
.tablet-cam{left:596px;top:674px;width:4px;height:4px;border-radius:50%;background:#333}

/* footer */
.site-footer{left:0;top:992px;width:821px;height:176px;background:var(--footer)}
.footer-tab{left:391px;top:992px;width:44px;height:3px;background:var(--blue)}
.footer-brand{left:60px;top:1040px;font-size:10px;font-weight:500;color:var(--white);display:flex;align-items:center;gap:6px}
.footer-head{font-size:11px;font-weight:600;color:var(--white);top:1019px}
.footer-text{font-size:8.5px;line-height:17.4px;color:var(--footer-text)}
.footer-list{list-style:none}
.footer-list li::before{content:"• "}
.contact-row{display:flex;align-items:center;gap:10px;height:19px}
.social-links{left:606px;top:1112px;display:flex;gap:12px;font-size:8.5px;color:var(--footer-text)}
.social-links a::before{content:"";display:inline-block;width:6px;height:6px;border-radius:50%;background:var(--blue);margin-right:5px;vertical-align:1px}
.footer-base{left:0;top:1168px;width:821px;height:32px;background:var(--footer-base)}
.copyright{left:53px;top:1184px;font-size:8.5px;color:var(--footer-text)}
.privacy-link{right:53px;top:1184px;font-size:8.5px;color:var(--footer-text)}
</style>
</head>
<body>

<header class="abs site-header">
  <div class="abs brand"><span class="brand-dot"></span><span class="brand-name">Gladly Call Corwin<br>Consulting</span></div>
  <nav class="abs nav">
    <a class="active" href="#">Home</a>
    <a href="#">About Us</a>
    <a href="#">Our Services</a>
    <a href="#">Contact Us</a>
    <a href="#">Blog</a>
  </nav>
</header>

<section class="abs hero"></section>
<div class="abs hero-art" role="img" aria-label="Businessman holding a glowing globe surrounded by devices, charts and network lines"></div>
<h1 class="abs hero-title">GLADLY CALL<br>CORWIN</h1>
<p class="abs hero-sub">Making IT and Telecommunications<br>simple for business</p>
<a class="abs hero-btn" href="#">Ask!</a>
<div class="abs slider-dots"><span class="on"></span><span></span><span></span></div>

<section class="abs band-intro"></section>
<h2 class="abs section-title" style="top:412px">PERFECT SOLUTION</h2>
<p class="abs section-kicker" style="top:439px">For making IT and telecommunications simple for business</p>
<p class="abs intro-copy">Gladly Call Corwin is here to assist business in having a better understanding of Information Technology and Telecommunications products and services, and more importantly, how these products and services can be of benefit to your business. We can help you to assess what you have now, what your business needs are currently in terms of technology and where your business needs are heading in the future.</p>

<section class="abs band-features"></section>
<h2 class="abs section-title" style="top:576px">GLADLY CALL CORWIN</h2>
<p class="abs section-kicker" style="top:603px">For making IT and telecommunications simple for business</p>

<div class="abs feature-icon" style="left:54px;top:668px">
  <svg width="18" height="18" viewBox="0 0 18 18"><circle cx="9" cy="9" r="7.5" fill="none" stroke="#29a9e1" stroke-width="3"/><circle cx="9" cy="9" r="3" fill="#fff"/><path d="M9 1.5v3M9 13.5v3M1.5 9h3M13.5 9h3" stroke="#fff" stroke-width="2"/></svg>
</div>
<h3 class="abs feature-title" style="top:667px">What can we help with</h3>
<p class="abs feature-copy" style="top:683px">Quisque posuere dolor quis varius sodales. Cras pretium quam eu quam venenatis tincidunt. Duis tempor iaculis turpis. Duis ac consequat massa, consectetur luctus lectus.</p>

<div class="abs feature-icon" style="left:54px;top:772px">
  <svg width="18" height="18" viewBox="0 0 18 18"><circle cx="9" cy="10" r="6.5" fill="none" stroke="#29a9e1" stroke-width="2"/><path d="M9 10l3-3" stroke="#29a9e1" stroke-width="2"/><path d="M7 2h4" stroke="#29a9e1" stroke-width="2"/></svg>
</div>
<h3 class="abs feature-title" style="top:771px">How can we help</h3>
<p class="abs feature-copy" style="top:788px">Quisque posuere dolor quis varius sodales. Cras pretium quam eu quam venenatis tincidunt. Duis tempor iaculis turpis. Duis ac consequat massa, consectetur luctus lectus.</p>

<div class="abs feature-icon" style="left:54px;top:877px">
  <svg width="18" height="16" viewBox="0 0 18 16"><path d="M1 6c0-3 16-3 16 0v2h-4V6H5v2H1z" fill="#29a9e1"/><path d="M4 9h10l2 6H2z" fill="#29a9e1"/><circle cx="9" cy="12" r="1.6" fill="#fff"/></svg>
</div>
<h3 class="abs feature-title" style="top:876px">Why not contact us</h3>
<p class="abs feature-copy" style="top:893px">Quisque posuere dolor quis varius sodales. Cras pretium quam eu quam venenatis tincidunt. Duis tempor iaculis turpis. Duis ac consequat massa, consectetur luctus lectus.</p>

<div class="abs tablet"></div>
<div class="abs tablet-cam"></div>
<div class="abs tablet-screen" role="img" aria-label="Businessman standing before a laptop surrounded by floating icons, charts and a world map"></div>

<footer class="abs site-footer"></footer>
<div class="abs footer-tab"></div>
<div class="abs footer-brand"><span class="brand-dot"></span><span>Gladly Call Corwin<br>Consulting</span></div>

<h4 class="abs footer-head" style="left:237px">GLADLY CALL CORWIN.</h4>
<p class="abs footer-text" style="left:237px;top:1040px;width:160px">Quisque posuere dolor quis varius sodales. Cras pretium quam eu quam venenatis tincidunt. Duis tempor iaculis turpis. Duis ac consequat massa.</p>

<h4 class="abs footer-head" style="left:422px">SITE</h4>
<ul class="abs footer-text footer-list" style="left:422px;top:1040px">
  <li>Home</li><li>About Us</li><li>Our Services</li><li>Contact Us</li><li>Blog</li>
</ul>

<h4 class="abs footer-head" style="left:606px">CONTACT</h4>
<div class="abs footer-text" style="left:606px;top:1040px">
  <div class="contact-row"><svg width="10" height="12" viewBox="0 0 10 12"><path d="M5 12S0 6.5 0 4.5a5 5 0 0110 0C10 6.5 5 12 5 12z" fill="#29a9e1"/><circle cx="5" cy="4.5" r="1.7" fill="#15232f"/></svg><span>214 Harbour Lane Westbay North SA</span></div>
  <div class="contact-row"><svg width="12" height="10" viewBox="0 0 18 16"><path d="M1 6c0-3 16-3 16 0v2h-4V6H5v2H1z" fill="#29a9e1"/><path d="M4 9h10l2 6H2z" fill="#29a9e1"/></svg><span>(08) 7000 0199</span></div>
  <div class="contact-row"><svg width="12" height="9" viewBox="0 0 12 9"><rect width="12" height="9" fill="#29a9e1"/><path d="M0 0l6 5 6-5" fill="none" stroke="#15232f" stroke-width="1"/></svg><span>hello@gladlycallcorwin.example</span></div>
</div>
<nav class="abs social-links">
  <a href="#">Chatterbook</a><a href="#">WorkWeave</a><a href="#">Quorra plus</a>
</nav>

<div class="abs footer-base"></div>
<p class="abs copyright">Gladly Call Corwin ©2014. All rights reserved.</p>
<a class="abs privacy-link" href="#">Privacy Policy</a>

</body>
</html>
```